Meridel Haulage - Website

A clean, not cluttered informative website for our business. We specialize in the transportation of radioactive materials across North America. The site is mostly for information about our company and will not be used to attract business but will be used to attract employee's mainly drivers. Driver's are very hard to find in our area. One of the pages needs to be a job's posting page with an apply now button. Either an application can be filled out there or a resume can be uploaded which ever functionality works better. I would like a website that I can easily edit, ability to change text and photos.

Number of Pages Required

5+ page

Colors

Designer to choose colors to be used in the design.

Requirements
Must have
• Home - About - Services - Jobs - Contact pages
• A way prospective employee's can apply or upload their resume to be emailed to me
• Very clean apperance
Should not have
• I don't want it to be busy

```html
<!DOCTYPE html>
<html lang="en">
<head>
<meta charset="utf-8">
<title>Meridel Haulage</title>
<link href="https://fonts.googleapis.com/css2?family=Montserrat:wght@500;600;700;800&family=Roboto:wght@300;400;500;700&display=swap" rel="stylesheet">
<style>
:root{
  --blue:#1e44b8;
  --blue-deep:#14318f;
  --navy:#0e2670;
  --navy-dark:#0a1d57;
  --orange:#f6a81c;
  --ink:#2b2f3a;
  --muted:#7b8190;
  --line:#e3e6ee;
  --pale:#f2f5fc;
  --white:#ffffff;
}
*{margin:0;padding:0;box-sizing:border-box}
html,body{width:1200px;height:3344px;overflow:hidden}
body{font-family:"Roboto",Arial,sans-serif;color:var(--ink);background:var(--white);position:relative;font-size:13px;line-height:1.6}
h1,h2,h3,h4{font-family:"Montserrat",Arial,sans-serif}
.wrap{width:1000px;margin:0 auto;position:relative}
.btn{display:inline-block;background:var(--orange);color:var(--white);font-weight:500;font-size:13px;padding:10px 26px;border-radius:2px}

/* top bar */
.topbar{height:24px;background:var(--navy-dark);color:#c8d2ef;font-size:11px;line-height:24px}
.topbar .wrap{display:flex;gap:30px}
/* header */
.header{height:76px}
.header .wrap{display:flex;align-items:center;height:76px;justify-content:space-between}
.brand{display:flex;align-items:center;gap:10px;font-family:"Montserrat",sans-serif;font-weight:700;font-size:20px;color:var(--blue)}
.brand .dot{width:14px;height:14px;background:var(--orange);border-radius:50%}
.contact-items{display:flex;gap:34px}
.contact-item{display:flex;align-items:center;gap:10px}
.contact-item svg{width:26px;height:26px}
.contact-item b{display:block;font-size:12px;font-weight:500;color:var(--ink)}
.contact-item span{display:block;font-size:11px;color:var(--orange)}

/* hero */
.hero{height:400px;position:relative;background:linear-gradient(180deg,#0f3d9a 0%,#3d7fd6 40%,#a9c9ee 75%,#e8f1fb 100%)}
.nav{position:absolute;left:240px;right:200px;top:0;height:46px;background:var(--blue);display:flex;gap:44px;padding-left:40px;align-items:center;z-index:2}
.nav a{color:var(--white);font-family:"Montserrat",sans-serif;font-weight:600;font-size:17px;text-decoration:none}
.hero-copy{position:absolute;top:110px;left:0;right:0;text-align:center;color:var(--white)}
.hero-copy h1{font-size:40px;font-weight:800;line-height:1.2;letter-spacing:1px;text-transform:uppercase}
.hero-copy p{margin-top:12px;font-size:14px;opacity:.9}
.hero-arrow{position:absolute;top:190px;width:26px;height:26px;background:rgba(255,255,255,.25);display:flex;align-items:center;justify-content:center}
.hero-arrow.left{left:14px}.hero-arrow.right{right:14px}

/* intro */
.intro{height:260px;background:var(--blue);color:var(--white);text-align:center;padding-top:50px}
.intro h2{font-size:24px;font-weight:600;line-height:1.35;width:620px;margin:0 auto}
.intro p{width:560px;margin:22px auto 24px;font-size:13px;color:#d8e1fa}

/* services */
.services{height:340px;padding-top:24px}
.services .wrap{display:grid;grid-template-columns:repeat(4,1fr);gap:20px}
.service-photo{height:150px}
.service-body{padding:0 14px 14px;text-align:center;border:1px solid var(--line);border-top:none}
.service-icon{width:44px;height:44px;border-radius:50%;background:var(--blue);margin:-22px auto 8px;display:flex;align-items:center;justify-content:center;border:3px solid var(--white)}
.service-body h3{font-size:14px;font-weight:600;color:var(--ink)}
.service-body p{font-size:11px;color:var(--muted);line-height:1.5;margin-top:4px}

/* why + jobs */
.why{height:460px;padding-top:40px}
.why .wrap{display:grid;grid-template-columns:300px 320px 340px;gap:20px}
.section-title{font-size:18px;font-weight:700;color:var(--ink);text-transform:uppercase;padding-bottom:10px;border-bottom:2px solid var(--line);margin-bottom:18px;position:relative}
.section-title::after{content:"";position:absolute;left:0;bottom:-2px;width:50px;height:2px;background:var(--orange)}
.jobs-title{font-size:24px;font-weight:600;color:var(--blue);text-transform:none;border:none;padding-bottom:0}
.jobs-title::after{display:none}
.reason{display:flex;gap:14px;margin-bottom:22px}
.reason svg{flex:none;width:28px;height:28px}
.reason h4{font-size:13px;font-weight:600}
.reason p{font-size:11px;color:var(--muted);line-height:1.5}
.job-form{display:grid;grid-template-columns:1fr 1fr;gap:10px;margin-top:16px}
.field{height:34px;border:1px solid var(--line);font-size:11px;color:var(--muted);padding:8px 10px}
.field.wide{grid-column:1/3;height:80px}
.job-form .btn{grid-column:1/2;width:110px;text-align:center;padding:9px 0;margin-top:4px}
.truck-photo{height:220px;margin-top:48px;background:linear-gradient(160deg,#cfd7e2 0%,#8d98a8 55%,#4d5564 100%)}

/* stats */
.stats{height:110px;background:var(--blue);color:var(--white)}
.stats .wrap{display:grid;grid-template-columns:repeat(4,1fr);height:110px;align-items:center}
.stat{display:flex;align-items:center;gap:12px;justify-content:center}
.stat svg{width:32px;height:32px}
.stat b{font-family:"Montserrat",sans-serif;font-size:30px;font-weight:600;line-height:1}
.stat span{font-size:11px;color:#d4ddf7;display:block}

/* team */
.team{height:440px;padding-top:40px}
.team-grid{display:grid;grid-template-columns:repeat(4,1fr);gap:26px;margin-top:26px}
.member-photo{height:160px;background:linear-gradient(180deg,#e4e9f2,#b9c3d3)}
.member{text-align:center}
.member h4{font-size:13px;font-weight:600;margin-top:10px}
.member span{font-size:11px;color:var(--orange)}
.team-note{text-align:center;font-size:12px;color:var(--muted);width:560px;margin:30px auto 0}

/* testimonials */
.testimonials{height:340px;background:linear-gradient(135deg,#0b2a8a 0%,#1e48c2 55%,#0d2f90 100%);padding-top:56px}
.testimonials .wrap{display:grid;grid-template-columns:1fr 1fr;gap:30px;width:760px}
.quote{border:1px solid rgba(255,255,255,.5);padding:22px 26px;color:var(--white);position:relative}
.stars{color:var(--orange);font-size:13px;letter-spacing:2px}
.quote p{font-style:italic;font-size:14px;line-height:1.55;margin:10px 0 12px}
.quote b{display:block;font-size:12px;font-weight:500}
.quote span{font-size:11px;color:var(--orange)}
.dots{display:flex;justify-content:center;gap:8px;margin-top:26px}
.dots i{width:7px;height:7px;border-radius:50%;background:rgba(255,255,255,.5)}
.dots i:first-child{background:var(--white)}

/* features */
.features{height:160px;background:var(--pale)}
.features .wrap{display:grid;grid-template-columns:repeat(3,1fr);height:160px;align-items:center;gap:30px}
.feature{display:flex;gap:14px;align-items:flex-start}
.feature svg{flex:none;width:34px;height:34px}
.feature h4{font-size:14px;font-weight:600;color:var(--blue)}
.feature p{font-size:11px;color:var(--muted);line-height:1.5}

/* map */
.map{height:260px;background:linear-gradient(135deg,#eceff2,#dde2e8);position:relative}
.map-pin{position:absolute;left:585px;top:100px}

/* footer */
.footer{height:464px;background:var(--navy);color:#c6d0ee;padding-top:50px;position:relative}
.footer .wrap{display:grid;grid-template-columns:1.3fr 1fr 1.3fr 1.3fr;gap:34px}
.footer h4{color:var(--white);font-size:15px;font-weight:600;margin-bottom:16px}
.footer p,.footer li{font-size:11px;line-height:1.7}
.footer ul{list-style:none}
.footer li{margin-bottom:4px}
.footer li::before{content:"› ";color:var(--orange)}
.post{margin-bottom:12px}
.post b{display:block;color:var(--white);font-weight:400;font-size:11px}
.post span{color:var(--orange);font-size:10px}
.subscribe{display:flex;margin:12px 0}
.subscribe .field{flex:1;background:var(--white);border:none}
.subscribe .btn{padding:8px 14px}
.socials{display:flex;gap:8px;margin-top:16px}
.socials i{width:26px;height:26px;background:var(--blue);border-radius:50%}
.copyright{position:absolute;left:0;right:0;bottom:0;height:44px;line-height:44px;background:var(--navy-dark);text-align:center;font-size:11px;color:#9eacd8}
</style>
</head>
<body>

<div class="topbar"><div class="wrap"><span>Tel: (555) 014-8820</span><span>Mon – Fri: 7:00 – 18:00 · Saturday closed</span></div></div>

<header class="header"><div class="wrap">
  <div class="brand"><span class="dot"></span>Meridel Haulage</div>
  <div class="contact-items">
    <div class="contact-item"><svg viewBox="0 0 24 24"><path d="M12 2a7 7 0 0 0-7 7c0 5 7 13 7 13s7-8 7-13a7 7 0 0 0-7-7zm0 9.5A2.5 2.5 0 1 1 12 6.5a2.5 2.5 0 0 1 0 5z" fill="#1e44b8"/></svg><div><b>Address / Head Office</b><span>48 Orchard Lane, Kestrel</span></div></div>
    <div class="contact-item"><svg viewBox="0 0 24 24"><path d="M6.6 10.8a15 15 0 0 0 6.6 6.6l2.2-2.2a1 1 0 0 1 1-.3 11 11 0 0 0 3.6.6 1 1 0 0 1 1 1V20a1 1 0 0 1-1 1A17 17 0 0 1 3 4a1 1 0 0 1 1-1h3.5a1 1 0 0 1 1 1 11 11 0 0 0 .6 3.6 1 1 0 0 1-.3 1z" fill="#1e44b8"/></svg><div><b>Toll Free Number</b><span>(555) 014-8820</span></div></div>
    <div class="contact-item"><svg viewBox="0 0 24 24"><circle cx="12" cy="12" r="9" fill="none" stroke="#1e44b8" stroke-width="2"/><path d="M12 7v5l3 2" stroke="#1e44b8" stroke-width="2" fill="none"/></svg><div><b>Opening Hours</b><span>Mon – Fri 7:00 – 18:00</span></div></div>
  </div>
</div></header>

<section class="hero" role="img" aria-label="Cargo aircraft flying above the clouds in a blue sky">
  <nav class="nav"><a>Home</a><a>About Us</a><a>Service</a><a>Jobs</a><a>Contact Us</a></nav>
  <div class="hero-arrow left"><svg width="10" height="10" viewBox="0 0 10 10"><path d="M7 1 3 5l4 4" stroke="#fff" stroke-width="2" fill="none"/></svg></div>
  <div class="hero-arrow right"><svg width="10" height="10" viewBox="0 0 10 10"><path d="M3 1l4 4-4 4" stroke="#fff" stroke-width="2" fill="none"/></svg></div>
  <div class="hero-copy">
    <h1>Providing First<br>Class Freight Services</h1>
    <p>Safe and compliant transport of sensitive materials<br>across North America, mile after mile.</p>
  </div>
</section>

<section class="intro">
  <h2>Meridel Haulage is a Global Supplier of Transport and logistics Solutions.</h2>
  <p>Incorporated in 1998, Meridel Haulage has used its local expertise to move specialised loads safely and serve an ever expanding network of customers.</p>
  <span class="btn">Read More</span>
</section>

<section class="services"><div class="wrap">
  <article class="service"><div class="service-photo" role="img" aria-label="Cargo plane at sunset" style="background:linear-gradient(180deg,#f3b96a,#a86a4a)"></div><div class="service-body"><div class="service-icon"><svg width="20" height="20" viewBox="0 0 24 24"><path d="M2 14l20-6-4 10-6-3-3 4v-5z" fill="#fff"/></svg></div><h3>Air Forwarding</h3><p>Our careful routing keeps urgent air freight on time and fully tracked.</p></div></article>
  <article class="service"><div class="service-photo" role="img" aria-label="Container ship at sea" style="background:linear-gradient(180deg,#8fc1ea,#2f6fb3)"></div><div class="service-body"><div class="service-icon"><svg width="20" height="20" viewBox="0 0 24 24"><path d="M3 14h18l-3 6H6zM7 8h10v6H7z" fill="#fff"/></svg></div><h3>Water Forwarding</h3><p>Reliable sea freight with secure handling from port to final destination.</p></div></article>
  <article class="service"><div class="service-photo" role="img" aria-label="Truck on a highway" style="background:linear-gradient(180deg,#9fc2e4,#5b6f86)"></div><div class="service-body"><div class="service-icon"><svg width="20" height="20" viewBox="0 0 24 24"><path d="M2 6h12v10H2zM14 10h4l3 3v3h-7z" fill="#fff"/><circle cx="6" cy="18" r="2" fill="#fff"/><circle cx="17" cy="18" r="2" fill="#fff"/></svg></div><h3>Road Forwarding</h3><p>Licensed drivers move your loads safely on every North American route.</p></div></article>
  <article class="service"><div class="service-photo" role="img" aria-label="Warehouse with stacked goods" style="background:linear-gradient(180deg,#e9c98c,#8a6a3e)"></div><div class="service-body"><div class="service-icon"><svg width="20" height="20" viewBox="0 0 24 24"><path d="M2 9l10-6 10 6v12H2zM7 13h10v8H7z" fill="#fff"/></svg></div><h3>Warehousing</h3><p>Secure, monitored storage facilities built for sensitive cargo.</p></div></article>
</div></section>

<section class="why"><div class="wrap">
  <div>
    <h2 class="section-title">Why Choosing Us?</h2>
    <div class="reason"><svg viewBox="0 0 24 24"><circle cx="12" cy="12" r="10" fill="none" stroke="#1e44b8" stroke-width="2"/><path d="M2 12h20M12 2c3 3 3 17 0 20M12 2c-3 3-3 17 0 20" stroke="#1e44b8" stroke-width="1.5" fill="none"/></svg><div><h4>Global Supply Chain Solutions</h4><p>We plan every route end to end so each load arrives safely.</p></div></div>
    <div class="reason"><svg viewBox="0 0 24 24"><circle cx="12" cy="12" r="10" fill="none" stroke="#1e44b8" stroke-width="2"/><path d="M12 6v6l4 2" stroke="#1e44b8" stroke-width="2" fill="none"/></svg><div><h4>24 Hours - Technical Support</h4><p>Our dispatch team answers drivers and clients around the clock.</p></div></div>
    <div class="reason"><svg viewBox="0 0 24 24"><rect x="6" y="2" width="12" height="20" rx="2" fill="none" stroke="#1e44b8" stroke-width="2"/><circle cx="12" cy="18" r="1.2" fill="#1e44b8"/></svg><div><h4>Mobile Shipment Tracking</h4><p>Follow each shipment live from pickup to delivery on any device.</p></div></div>
    <div class="reason"><svg viewBox="0 0 24 24"><path d="M3 8l9-5 9 5v9l-9 5-9-5z" fill="none" stroke="#1e44b8" stroke-width="2"/></svg><div><h4>Careful Handling of Valuable Goods</h4><p>Trained crews follow strict safety rules for sensitive material.</p></div></div>
  </div>
  <div>
    <h2 class="section-title jobs-title">Find Driving Jobs</h2>
    <div class="job-form">
      <div class="field">First Name</div><div class="field">Last Name</div>
      <div class="field">Email</div><div class="field">Phone</div>
      <div class="field">Licence Class</div><div class="field">Upload Resume</div>
      <div class="field wide">Message</div>
      <span class="btn">Apply Now</span>
    </div>
  </div>
  <div class="truck-photo" role="img" aria-label="Tanker truck parked in a yard"></div>
</div></section>

<section class="stats"><div class="wrap">
  <div class="stat"><svg viewBox="0 0 24 24"><path d="M3 7l9-4 9 4v10l-9 4-9-4z" fill="none" stroke="#fff" stroke-width="1.6"/></svg><div><b>9800</b><span>Delivered Package</span></div></div>
  <div class="stat"><svg viewBox="0 0 24 24"><circle cx="12" cy="12" r="9" fill="none" stroke="#fff" stroke-width="1.6"/><path d="M3 12h18M12 3v18" stroke="#fff" stroke-width="1.2"/></svg><div><b>230</b><span>Office Worldwide</span></div></div>
  <div class="stat"><svg viewBox="0 0 24 24"><circle cx="12" cy="8" r="4" fill="none" stroke="#fff" stroke-width="1.6"/><path d="M4 21c0-5 16-5 16 0" fill="none" stroke="#fff" stroke-width="1.6"/></svg><div><b>1200</b><span>Company Staffs</span></div></div>
  <div class="stat"><svg viewBox="0 0 24 24"><path d="M2 6h12v10H2zM14 10h4l3 3v3h-7z" fill="none" stroke="#fff" stroke-width="1.6"/></svg><div><b>5200</b><span>Tons of Goods</span></div></div>
</div></section>

<section class="team"><div class="wrap">
  <h2 class="section-title">Meet Our Team</h2>
  <div class="team-grid">
    <div class="member"><div class="member-photo" role="img" aria-label="Portrait of team member"></div><h4>Daniel Hartley</h4><span>Fleet Manager</span></div>
    <div class="member"><div class="member-photo" role="img" aria-label="Portrait of team member"></div><h4>Nora Calloway</h4><span>Safety Officer</span></div>
    <div class="member"><div class="member-photo" role="img" aria-label="Portrait of team member"></div><h4>Ivy Marston</h4><span>Dispatch Lead</span></div>
    <div class="member"><div class="member-photo" role="img" aria-label="Portrait of team member"></div><h4>Owen Pratt</h4><span>Senior Driver</span></div>
  </div>
  <p class="team-note">We're always looking for talented transporters, creative thinkers and people that have a passion for the open road and safe delivery.</p>
</div></section>

<section class="testimonials"><div class="wrap">
  <div class="quote"><div class="stars">★★★★★</div><p>"The shipping process with this crew was a pleasurable experience! They did all in time and with no safety incidents. Thank you so much guys!"</p><b>Clara Benning</b><span>Plant Supervisor</span></div>
  <div class="quote"><div class="stars">★★★★★</div><p>"These guys are just the coolest company ever! They were aware of our timetable for road and rail and made no mistake in every load."</p><b>Rosa Delmare</b><span>Logistics Director</span></div>
</div><div class="dots"><i></i><i></i></div></section>

<section class="features"><div class="wrap">
  <div class="feature"><svg viewBox="0 0 24 24"><path d="M2 12h12M5 8h9M8 16h6M14 6h4l4 6-4 6h-4z" fill="none" stroke="#1e44b8" stroke-width="1.8"/></svg><div><h4>Fast worldwide delivery</h4><p>Planned routes and experienced drivers keep every delivery moving on schedule.</p></div></div>
  <div class="feature"><svg viewBox="0 0 24 24"><path d="M4 14v-2a8 8 0 0 1 16 0v2M4 14h3v5H4zM17 14h3v5h-3z" fill="none" stroke="#1e44b8" stroke-width="1.8"/></svg><div><h4>24/7 customer support</h4><p>Our dispatch desk is staffed day and night for drivers and clients alike.</p></div></div>
  <div class="feature"><svg viewBox="0 0 24 24"><path d="M12 2l8 3v6c0 5-3.5 9-8 11-4.5-2-8-6-8-11V5z" fill="none" stroke="#1e44b8" stroke-width="1.8"/><path d="M8 12l3 3 5-6" fill="none" stroke="#1e44b8" stroke-width="1.8"/></svg><div><h4>Safe and Secure</h4><p>Every load follows strict federal safety rules, checks and full documentation.</p></div></div>
</div></section>

<section class="map" role="img" aria-label="Street map showing the head office location">
  <svg class="map-pin" width="30" height="40" viewBox="0 0 24 32"><path d="M12 0a11 11 0 0 0-11 11c0 8 11 21 11 21s11-13 11-21A11 11 0 0 0 12 0z" fill="#1e44b8"/><circle cx="12" cy="11" r="4" fill="#f6a81c"/></svg>
</section>

<footer class="footer"><div class="wrap">
  <div><h4>About Meridel</h4><p>Meridel Haulage moves sensitive and regulated freight across North America with trained, licensed drivers and a strong focus on safety.</p><div class="socials"><i></i><i></i><i></i><i></i></div></div>
  <div><h4>Useful Links</h4><ul><li>All Services</li><li>Ground Transport</li><li>Cargo Services</li><li>Warehousing</li><li>Road Freight Services</li><li>Driver Job Openings</li></ul></div>
  <div><h4>Recent Posts</h4>
    <div class="post"><b>New driver training program opens this spring</b><span>August 8, 2017</span></div>
    <div class="post"><b>How we keep every route safe and compliant</b><span>August 5, 2017</span></div>
    <div class="post"><b>Meet the dispatch team behind the fleet</b><span>July 29, 2017</span></div>
    <div class="post"><b>Introducing our new tanker trailers</b><span>July 21, 2017</span></div>
  </div>
  <div><h4>Our Newsletter</h4><p>Sign up today for the latest news, job openings and updates from our team.</p><div class="subscribe"><div class="field">Enter Your Email</div><span class="btn">Send</span></div><p>We don't share your email with anyone else.</p></div>
</div>
<div class="copyright">© 2017 Meridel Haulage. All rights reserved.</div>
</footer>

</body>
</html>
```